Verdanix Medical Business Card

Create a high class Business card for Medical Aesthetics and Wellness Practice called Verdanix Medical Aesthetics and Wellness as per the logo attached.
Addresss is: 418 Harlan Brook Road Suite 312 Corwen Falls, Westmere 11093
Phone (555)204-7391 IG @verdanix_medical
Verdanixmedical.example

I need 5 different name configurations
1) Dr. Theo Valcourt
Aesthetics and Wellness Specialist
Medical Director

2) Rosalind Pettinger, NP
Clinical Nurse Manager

3) Marla Vostrik, RN
Aesthetic Nurse Specialist

4) Petra Halvesen, RN

5) Dana Kowbeck, L.E.
Senior Licensed Esthetician

Target Market(s)

22-55 Females

Industry/Entity Type

Medical Spa and Wellness

Contact Information for Business Card

Logo, address, phone, web, instagram, providers name

Requirements
Must have
• Attractive classy modern look

```html
<!DOCTYPE html>
<html lang="en">
<head>
<meta charset="utf-8">
<title>Verdanix Medical – Business Cards</title>
<link rel="stylesheet" href="https://fonts.googleapis.com/css2?family=Cormorant+Garamond:wght@400;500&family=EB+Garamond:wght@400;500&display=swap">
<style>
  :root {
    --teal: #174c5f;
    --teal-deep: #0f3444;
    --paper: #ffffff;
    --page: #ffffff;
    --ink: #174c5f;
  }
  * { box-sizing: border-box; margin: 0; padding: 0; }
  html, body { width: 1200px; height: 2172px; overflow: hidden; background: var(--page); }
  body { position: relative; font-family: "EB Garamond", Georgia, serif; color: var(--ink); }

  .showcase {
    position: absolute; left: 0; top: 0; width: 1200px; height: 950px;
    background: var(--teal-deep);
  }

  .card { position: absolute; overflow: hidden; }
  .card--front { background: var(--teal); color: var(--paper); }
  .card--back { background: var(--paper); border: 1px solid var(--teal); color: var(--ink); }
  .card--lg { width: 520px; height: 312px; font-size: 11.5px; }
  .card--md { width: 452px; height: 272px; font-size: 10px; }
  .card--sm { width: 399px; height: 240px; font-size: 8.8px; }
  .showcase .card { box-shadow: 0 18px 40px rgba(0,0,0,.45); }

  .brand { position: absolute; left: 0; right: 0; top: 40%; text-align: center; }
  .brand__name {
    font-family: "Cormorant Garamond", Georgia, serif; font-weight: 400;
    font-size: 2.9em; letter-spacing: .12em; line-height: 1;
  }
  .brand__tagline { font-size: .78em; letter-spacing: .06em; text-transform: uppercase; margin-top: .5em; }
  .brand__city { font-size: .55em; letter-spacing: .6em; text-transform: uppercase; margin-top: .6em; }
  .website { position: absolute; left: 0; right: 0; top: 87%; text-align: center; font-size: 1.15em; letter-spacing: .02em; }

  .person { position: absolute; left: 0; right: 0; top: 40%; text-align: center; padding-left: 8%; }
  .person__name { font-size: 2.3em; letter-spacing: -.02em; line-height: 1; white-space: nowrap; }
  .person__name .bracket { font-family: "Cormorant Garamond", Georgia, serif; font-size: 1.15em; }
  .person__role { font-size: .8em; text-transform: uppercase; letter-spacing: .03em; margin-top: .6em; line-height: 1.5; }
  .person__sub { font-size: .62em; text-transform: uppercase; margin-top: .5em; }

  .contact { position: absolute; left: 16%; top: 75%; list-style: none; font-size: .72em; text-transform: uppercase; white-space: nowrap; }
  .contact li { display: flex; align-items: center; gap: .7em; height: 1.95em; }
  .contact svg { width: 1.4em; height: 1.4em; flex: none; }
</style>
</head>
<body>

<section class="showcase" aria-label="Card set presentation">
  <article class="card card--front card--lg" style="left:60px; top:300px;">
    <div class="brand">
      <div class="brand__name">Verdanix</div>
      <div class="brand__tagline">Medical Aesthetics and Wellness</div>
      <div class="brand__city">Corwen Falls</div>
    </div>
    <div class="website">www.verdanixmedical.example</div>
  </article>
  <article class="card card--back card--lg" style="left:620px; top:300px;">
    <div class="person">
      <div class="person__name"><span class="bracket">[</span> Dr. Theo Valcourt <span class="bracket">]</span></div>
      <div class="person__role">Aesthetics and Wellness Specialist</div>
      <div class="person__sub">Medical Director</div>
    </div>
    <ul class="contact">
      <li><svg viewBox="0 0 16 16" fill="none" stroke="currentColor" stroke-width="1.2"><path d="M8 14s4.5-4.3 4.5-7.5a4.5 4.5 0 0 0-9 0C3.5 9.7 8 14 8 14z"/><circle cx="8" cy="6.5" r="1.6"/></svg>418 Harlan Brook Road Suite 312 Corwen Falls, Westmere 11093</li>
      <li><svg viewBox="0 0 16 16" fill="none" stroke="currentColor" stroke-width="1.2"><path d="M4 2.5l2 2.5-1.2 1.6a8 8 0 0 0 4.6 4.6L11 10l2.5 2-1.2 1.8C7.3 13.5 2.5 8.7 2.2 3.7z"/></svg>(555)204-7391</li>
      <li><svg viewBox="0 0 16 16" fill="none" stroke="currentColor" stroke-width="1.2"><rect x="3" y="3" width="10" height="10"/></svg>@verdanix_medical</li>
    </ul>
  </article>
</section>

<article class="card card--front card--md" style="left:142px; top:1080px;">
  <div class="brand">
    <div class="brand__name">Verdanix</div>
    <div class="brand__tagline">Medical Aesthetics and Wellness</div>
    <div class="brand__city">Corwen Falls</div>
  </div>
  <div class="website">www.verdanixmedical.example</div>
</article>

<article class="card card--back card--md" style="left:605px; top:1080px;">
  <div class="person">
    <div class="person__name"><span class="bracket">[</span> Dr. Theo Valcourt <span class="bracket">]</span></div>
    <div class="person__role">Aesthetics and Wellness Specialist</div>
    <div class="person__sub">Medical Director</div>
  </div>
  <ul class="contact">
    <li><svg viewBox="0 0 16 16" fill="none" stroke="currentColor" stroke-width="1.2"><path d="M8 14s4.5-4.3 4.5-7.5a4.5 4.5 0 0 0-9 0C3.5 9.7 8 14 8 14z"/><circle cx="8" cy="6.5" r="1.6"/></svg>418 Harlan Brook Road Suite 312 Corwen Falls, Westmere 11093</li>
    <li><svg viewBox="0 0 16 16" fill="none" stroke="currentColor" stroke-width="1.2"><path d="M4 2.5l2 2.5-1.2 1.6a8 8 0 0 0 4.6 4.6L11 10l2.5 2-1.2 1.8C7.3 13.5 2.5 8.7 2.2 3.7z"/></svg>(555)204-7391</li>
    <li><svg viewBox="0 0 16 16" fill="none" stroke="currentColor" stroke-width="1.2"><rect x="3" y="3" width="10" height="10"/></svg>@verdanix_medical</li>
  </ul>
</article>

<article class="card card--back card--sm" style="left:192px; top:1448px;">
  <div class="person">
    <div class="person__name"><span class="bracket">[</span> Rosalind Pettinger, NP <span class="bracket">]</span></div>
    <div class="person__role">Clinical Nurse<br>Manager</div>
  </div>
  <ul class="contact">
    <li><svg viewBox="0 0 16 16" fill="none" stroke="currentColor" stroke-width="1.2"><path d="M8 14s4.5-4.3 4.5-7.5a4.5 4.5 0 0 0-9 0C3.5 9.7 8 14 8 14z"/><circle cx="8" cy="6.5" r="1.6"/></svg>418 Harlan Brook Road Suite 312 Corwen Falls, Westmere 11093</li>
    <li><svg viewBox="0 0 16 16" fill="none" stroke="currentColor" stroke-width="1.2"><path d="M4 2.5l2 2.5-1.2 1.6a8 8 0 0 0 4.6 4.6L11 10l2.5 2-1.2 1.8C7.3 13.5 2.5 8.7 2.2 3.7z"/></svg>(555)204-7391</li>
    <li><svg viewBox="0 0 16 16" fill="none" stroke="currentColor" stroke-width="1.2"><rect x="3" y="3" width="10" height="10"/></svg>@verdanix_medical</li>
  </ul>
</article>

<article class="card card--back card--sm" style="left:604px; top:1448px;">
  <div class="person">
    <div class="person__name"><span class="bracket">[</span> Marla Vostrik, RN <span class="bracket">]</span></div>
    <div class="person__role">Aesthetic Nurse<br>Specialist</div>
  </div>
  <ul class="contact">
    <li><svg viewBox="0 0 16 16" fill="none" stroke="currentColor" stroke-width="1.2"><path d="M8 14s4.5-4.3 4.5-7.5a4.5 4.5 0 0 0-9 0C3.5 9.7 8 14 8 14z"/><circle cx="8" cy="6.5" r="1.6"/></svg>418 Harlan Brook Road Suite 312 Corwen Falls, Westmere 11093</li>
    <li><svg viewBox="0 0 16 16" fill="none" stroke="currentColor" stroke-width="1.2"><path d="M4 2.5l2 2.5-1.2 1.6a8 8 0 0 0 4.6 4.6L11 10l2.5 2-1.2 1.8C7.3 13.5 2.5 8.7 2.2 3.7z"/></svg>(555)204-7391</li>
    <li><svg viewBox="0 0 16 16" fill="none" stroke="currentColor" stroke-width="1.2"><rect x="3" y="3" width="10" height="10"/></svg>@verdanix_medical</li>
  </ul>
</article>

<article class="card card--back card--sm" style="left:192px; top:1717px;">
  <div class="person">
    <div class="person__name"><span class="bracket">[</span> Petra Halvesen, RN <span class="bracket">]</span></div>
    <div class="person__role">Aesthetic Nurse Specialist</div>
  </div>
  <ul class="contact">
    <li><svg viewBox="0 0 16 16" fill="none" stroke="currentColor" stroke-width="1.2"><path d="M8 14s4.5-4.3 4.5-7.5a4.5 4.5 0 0 0-9 0C3.5 9.7 8 14 8 14z"/><circle cx="8" cy="6.5" r="1.6"/></svg>418 Harlan Brook Road Suite 312 Corwen Falls, Westmere 11093</li>
    <li><svg viewBox="0 0 16 16" fill="none" stroke="currentColor" stroke-width="1.2"><path d="M4 2.5l2 2.5-1.2 1.6a8 8 0 0 0 4.6 4.6L11 10l2.5 2-1.2 1.8C7.3 13.5 2.5 8.7 2.2 3.7z"/></svg>(555)204-7391</li>
    <li><svg viewBox="0 0 16 16" fill="none" stroke="currentColor" stroke-width="1.2"><rect x="3" y="3" width="10" height="10"/></svg>@verdanix_medical</li>
  </ul>
</article>

<article class="card card--back card--sm" style="left:604px; top:1717px;">
  <div class="person">
    <div class="person__name"><span class="bracket">[</span> Dana Kowbeck, L.E. <span class="bracket">]</span></div>
    <div class="person__role">Senior Licensed Esthetician</div>
  </div>
  <ul class="contact">
    <li><svg viewBox="0 0 16 16" fill="none" stroke="currentColor" stroke-width="1.2"><path d="M8 14s4.5-4.3 4.5-7.5a4.5 4.5 0 0 0-9 0C3.5 9.7 8 14 8 14z"/><circle cx="8" cy="6.5" r="1.6"/></svg>418 Harlan Brook Road Suite 312 Corwen Falls, Westmere 11093</li>
    <li><svg viewBox="0 0 16 16" fill="none" stroke="currentColor" stroke-width="1.2"><path d="M4 2.5l2 2.5-1.2 1.6a8 8 0 0 0 4.6 4.6L11 10l2.5 2-1.2 1.8C7.3 13.5 2.5 8.7 2.2 3.7z"/></svg>(555)204-7391</li>
    <li><svg viewBox="0 0 16 16" fill="none" stroke="currentColor" stroke-width="1.2"><rect x="3" y="3" width="10" height="10"/></svg>@verdanix_medical</li>
  </ul>
</article>

</body>
</html>
```